banner for website

I need a new banner for my website. My website now is. www.brightmeadowkitchenway.com, but I'm changing it to Verdant Daily Table and I need a new banner. I want me to be who it's about. I am my brand. I'm Marla Pennick. So, my name needs to be prominent in the banner along with my photo, which I'm attaching. I want my photo very prominent in the banner and very large. I am attaching my two favorites.
I need the banner plain ( with out the newsletter sign up optin part), so I can use it on my newsletters, emails and letter head, as well. I would like it to be inviting. I I have a certain color scheme I use. Deep dark brown letters with blues and greens. Very earthy and psychologically grounded. I would like to keep that color scheme. In my website banner, I need a opt in to sign up for my free monthly newsletter and receive my Free Pantry Basket Planner.

I want the shopping guide to be small and pleasant looking and to say: "Sign up to receive your Free Pantry Basket Planner and monthly newsletter."

I only want my banner to say: "Verdant Daily Table" "Marla Pennick"

I would also like to have part of the banner without the sign in for the newsletter part off of it. And also one with only the "Verdant Daily Table" and one with "Verdant Daily Table" and "Marla Pennick" without the newsletter sign up part on it either.

I hope you can do this for me. I look forward to seeing your design! Sincerely, Marla
Updates

Project Deadline Extended Reason: I couldn't view the designs so I couldn't look at the ones submitted. I just now got into the website with your company's help. I don't want to be penalized because of a problem with the log in at your site. That was not my fault. Please let me know your thoughts. Added Monday, May 9, 2016

Target Market(s)

people over 40 who have bad health or who want to learn how to be a vegetarian for better health.

Number of Pages Required

1 page

Requirements
Must have
• I want the shopping guide to be small and pleasant looking and to say: "Sign up to receive your Free Pantry Basket Planner and monthly newsletter." I would like it to blend and be elegant and not in the middle of the banner or across my face.
• I only want my banner to say: "Verdant Daily Table" "Marla Pennick"
• I would also like to have part of the banner without the sign in for the newsletter part off of it. And also one with only the "Verdant Daily Table" and one with "Verdant Daily Table" and "Marla Pennick" without the newsletter sign up part on it either.
Nice to have
• Nice font and colors. I want the background to be plants and earthy and inviting.
Should not have
• I updated and added two new photos. I think the one you were using with me in the red top looked funny under my eyes. it was too pink or something. I uploaded a better version of that photo. in hopes that it looks better. Please switch those out if you are using the one with me in the red top.

```html
<!DOCTYPE html>
<html lang="en">
<head>
<meta charset="utf-8">
<title>Verdant Daily Table – Website Banners</title>
<link rel="stylesheet" href="https://fonts.googleapis.com/css2?family=Roboto+Condensed:wght@300&family=Jost:wght@400&family=Kaushan+Script&display=swap">
<style>
  :root {
    --page-bg: #ffffff;
    --brown-deep: #4a1a0c;
    --brown-caption: #6b2e17;
    --sky-top: #35b3ee;
    --sky-light: #bfe6fb;
    --haze: #eef6fb;
    --meadow: #8fd07a;
    --meadow-deep: #3fae45;
    --copper-light: #e7b093;
    --copper-mid: #a8552f;
    --copper-dark: #6e2a12;
    --photo-hair: #d9b98a;
    --photo-skin: #eab79b;
    --photo-shirt: #f4f1ec;
  }
  * { margin: 0; padding: 0; box-sizing: border-box; }
  html, body {
    width: 1000px; height: 1200px; overflow: hidden;
    background: var(--page-bg);
  }
  .sheet { position: relative; width: 1000px; height: 1200px; }

  .banner {
    position: absolute; left: 0; width: 1000px; height: 418px; overflow: hidden;
    background:
      radial-gradient(circle at 82% 12%, #ffffff 0, rgba(255,255,255,0.95) 60px, rgba(255,255,255,0.5) 160px, rgba(255,255,255,0) 330px),
      linear-gradient(180deg, var(--sky-top) 0%, var(--sky-light) 38%, var(--haze) 55%, var(--meadow) 75%, var(--meadow-deep) 100%);
  }
  .banner--title { top: 47px; }
  .banner--name { top: 555px; height: 420px; }

  .portrait {
    position: absolute; left: 0; top: 18px; width: 430px; height: 100%;
    border-radius: 46% 40% 0 0 / 30% 28% 0 0;
    background:
      radial-gradient(ellipse 95px 120px at 195px 175px, var(--photo-skin) 0, var(--photo-skin) 70%, rgba(234,183,155,0) 100%),
      radial-gradient(ellipse 160px 90px at 230px 400px, var(--photo-shirt) 0, var(--photo-shirt) 60%, rgba(244,241,236,0) 100%),
      linear-gradient(160deg, #e8cfa4 0%, var(--photo-hair) 45%, #b8946a 100%);
  }

  .banner-title {
    position: absolute; left: 364px; top: 200px;
    font-family: "Roboto Condensed", "Arial Narrow", sans-serif;
    font-weight: 300; font-size: 82px; line-height: 1; letter-spacing: -1px;
    color: var(--brown-deep);
    text-shadow: 2px 2px 0 #fff, -1px -1px 0 #fff, 1px -1px 0 #fff, -1px 1px 0 #fff, 3px 3px 4px rgba(0,0,0,0.15);
    white-space: nowrap;
  }

  .banner-name {
    position: absolute; left: 428px; top: 110px;
    font-family: "Kaushan Script", cursive;
    font-size: 118px; line-height: 112px;
    background: linear-gradient(180deg, var(--copper-light) 0%, var(--copper-mid) 45%, var(--copper-dark) 100%);
    -webkit-background-clip: text; background-clip: text;
    color: transparent;
    filter: drop-shadow(5px 4px 0 rgba(255,255,255,0.9)) drop-shadow(2px 3px 3px rgba(0,0,0,0.2));
    white-space: nowrap;
  }
  .banner-name span { display: block; }
  .banner-name .surname { margin-left: 10px; }

  .caption {
    position: absolute; left: 0; width: 1000px; text-align: center;
    font-family: "Jost", "Futura", sans-serif; font-weight: 400;
    font-size: 29px; color: var(--brown-caption); letter-spacing: 0;
  }
  .caption--title { top: 472px; }
  .caption--name { top: 985px; }
</style>
</head>
<body>
<main class="sheet">
  <section class="banner banner--title">
    <div class="portrait" role="img" aria-label="Portrait photo of Marla Pennick, smiling, with long blonde hair and a white blouse"></div>
    <h1 class="banner-title">Verdant Daily Table</h1>
  </section>
  <p class="caption caption--title">VERDANT DAILY TABLE</p>

  <section class="banner banner--name">
    <div class="portrait" role="img" aria-label="Portrait photo of Marla Pennick, smiling, with long blonde hair and a white blouse"></div>
    <h2 class="banner-name"><span class="given">Marla</span><span class="surname">Pennick</span></h2>
  </section>
  <p class="caption caption--name">MARLA PENNICK</p>
</main>
</body>
</html>
```